Motor Mate 4x6 Flyer

Need 4 x 6 Flyer with following language:

Willow Crest Motor Mate
Our Motor Mate Will Come to Your Home
Our Motor Mate will Drive Your Car to Nearest Gas Station
Our Motor Mate will Fill-up Your Car with Gas
Our Motor Mate will Immediately Return Your Car
Your Car Covered with $100k of Commercial Insurance
Member Dunmore Chamber of Commerce / Honest Merchant League
www.willowcrestmotormate.example

Place logos of Vortan, Brenn & Dorvane on Left Side of Flyer starting at top left corner, mid left side, left bottom corner.
Place logos of BoltNest, 12-Forty, Tesmira on opposite side right.....
Place Willow Crest Motor Mate Logo on both sides of very top that says Willow Crest Motor Mate

Target Market(s)

Upscale Home Owners

Font styles to use
Sans Serif

Colors
F0912C
F2A743
F7CA91
FBE8D2
FDF5EE

Requirements
Must have
• Flyer Must be Bright Orange

```html
<!DOCTYPE html>
<html lang="en">
<head>
<meta charset="utf-8">
<title>Willow Crest Motor Mate Flyer</title>
<link href="https://fonts.googleapis.com/css2?family=Bebas+Neue&family=Pathway+Gothic+One&family=Roboto:ital,wght@0,400;0,900;1,900&display=swap" rel="stylesheet">
<style>
  :root {
    --stage: #4b4b4b;
    --orange: #ff4400;
    --orange-deep: #bf3303;
    --orange-light: #ff8a5c;
    --ink: #111111;
    --ink-soft: #2b2b2b;
    --white: #ffffff;
    --paper-top: #ffffff;
    --paper-bottom: #8f8f8f;
    --cap: #c9c9c9;
    --hose: #3a3431;
  }
  * { box-sizing: border-box; margin: 0; padding: 0; }
  html, body { width: 1200px; height: 973px; overflow: hidden; }
  body { background: var(--stage); position: relative; }

  .flyer {
    position: absolute; left: 325px; top: 75px;
    width: 550px; height: 823px; overflow: hidden;
    background: linear-gradient(180deg, var(--paper-top) 0%, #e6e6e6 60%, var(--paper-bottom) 100%);
  }

  .brand-mark {
    position: absolute; top: 18px; width: 140px;
    display: flex; flex-direction: column; align-items: center; gap: 14px;
  }
  .brand-mark--left { left: 8px; }
  .brand-mark--right { left: 400px; }
  .brand-mark__square {
    width: 38px; height: 46px; border: 3px solid var(--orange); border-radius: 5px;
  }
  .brand-mark__name {
    font-family: "Roboto", sans-serif; font-weight: 400; font-size: 20px;
    color: var(--ink-soft); letter-spacing: 0.3px; white-space: nowrap;
  }

  .title-sign {
    position: absolute; left: 150px; top: 16px; width: 249px; height: 90px;
    border: 4px solid var(--ink); border-radius: 16px; background: var(--white);
    box-shadow: 2px 3px 0 #666;
    display: flex; flex-direction: column; align-items: center; justify-content: center;
    font-family: "Bebas Neue", sans-serif; font-weight: 400; font-size: 43px; line-height: 0.95;
    color: #222; text-align: center; white-space: nowrap;
  }

  .pump-cap {
    position: absolute; left: 126px; top: 113px; width: 300px; height: 30px;
    background: linear-gradient(90deg, #dadada, var(--cap) 60%, #b3b3b3);
    border-radius: 20px 20px 0 0;
  }
  .pump-body {
    position: absolute; left: 123px; top: 140px; width: 303px; height: 595px;
    border-radius: 0 0 12px 12px;
    background:
      radial-gradient(circle at 40% 42%, var(--orange) 0 62%, transparent 62.5%),
      linear-gradient(90deg, var(--orange-light) 0 5%, var(--orange-deep) 5% 100%);
  }

  .pump-panel {
    position: absolute; left: 139px; top: 156px; width: 271px; height: 481px;
    background: var(--white); border: 5px solid var(--ink); border-radius: 9px;
    padding: 12px 6px 0;
    display: flex; flex-direction: column; align-items: stretch;
  }
  .claim-head {
    display: flex; gap: 3px; width: 100%; height: 56px; flex: none;
  }
  .claim-head span {
    background: var(--ink); color: var(--white);
    font-family: "Bebas Neue", sans-serif; font-size: 50px; line-height: 56px;
    display: flex; align-items: center; justify-content: center;
    flex: 1 1 auto; min-width: 0; padding: 0 2px; white-space: nowrap;
  }
  .claim-text {
    font-family: "Pathway Gothic One", sans-serif; font-size: 31px; line-height: 31px;
    color: var(--ink); text-align: center; flex: none;
    display: flex; align-items: center; justify-content: center;
  }
  .claim-text--one { height: 41px; }
  .claim-text--two { height: 73px; }
  .claim-text--last { height: 72px; }

  .coverage {
    position: absolute; left: 123px; top: 640px; width: 303px;
    text-align: center; color: var(--white); font-family: "Roboto", sans-serif;
  }
  .coverage__line { font-size: 19px; font-weight: 400; line-height: 25px; }
  .coverage__amount { font-size: 30px; font-weight: 900; line-height: 34px; }

  .nozzle-art {
    position: absolute; left: 428px; top: 209px; width: 30px; height: 524px;
    background: linear-gradient(90deg, #5a5350, var(--hose) 50%, #8c8c8c);
    border-radius: 15px; opacity: 0.8;
  }

  .partner {
    position: absolute; z-index: 2;
    display: flex; align-items: center; justify-content: center; gap: 5px;
    width: 96px; height: 30px;
    font-family: "Roboto", sans-serif; font-weight: 900; font-size: 20px;
    white-space: nowrap;
  }
  .partner--vortan   { left: 13px;  top: 395px; color: #c8102e; }
  .partner--brenn    { left: 13px;  top: 484px; color: #d52b1e; }
  .partner--dorvane  { left: 13px;  top: 590px; color: #0072bc; }
  .partner--twelve   { left: 444px; top: 401px; color: #00804a; }
  .partner--tesmira  { left: 444px; top: 491px; color: #1b3f94; }
  .partner--boltnest { left: 444px; top: 583px; color: #c8102e; }
  .partner__dot { width: 10px; height: 10px; background: currentColor; border-radius: 50%; flex: none; }

  .footer-band {
    position: absolute; left: 24px; top: 736px; width: 502px; height: 87px;
    background: var(--orange); color: var(--white); text-align: center;
    display: flex; flex-direction: column; justify-content: center; gap: 4px;
  }
  .footer-band__member {
    font-family: "Pathway Gothic One", sans-serif; font-size: 21px; line-height: 26px;
    white-space: nowrap;
  }
  .footer-band__web {
    font-family: "Roboto", sans-serif; font-style: italic; font-weight: 900;
    font-size: 21px; line-height: 26px; white-space: nowrap;
  }
</style>
</head>
<body>
  <main class="flyer">
    <div class="brand-mark brand-mark--left">
      <span class="brand-mark__square"></span>
      <span class="brand-mark__name">MOTOR MATE</span>
    </div>
    <div class="brand-mark brand-mark--right">
      <span class="brand-mark__square"></span>
      <span class="brand-mark__name">MOTOR MATE</span>
    </div>

    <h1 class="title-sign"><span>Willow Crest</span><span>Motor Mate</span></h1>

    <div class="pump-cap"></div>
    <div class="pump-body"></div>
    <div class="nozzle-art" role="img" aria-label="Fuel pump nozzle and coiled hose illustration"></div>

    <section class="pump-panel">
      <div class="claim-head"><span>Our</span><span>Motor</span><span>Mate</span></div>
      <p class="claim-text claim-text--one">Will Come to Your Home</p>
      <div class="claim-head"><span>Our</span><span>Motor</span><span>Mate</span></div>
      <p class="claim-text claim-text--two">Will Drive Your Car to<br>Nearest Gas Station</p>
      <div class="claim-head"><span>Our</span><span>Motor</span><span>Mate</span></div>
      <p class="claim-text claim-text--one">Fill-up Your Car with Gas</p>
      <div class="claim-head"><span>Our</span><span>Motor</span><span>Mate</span></div>
      <p class="claim-text claim-text--last">Will Immediately Return<br>Your Car</p>
    </section>

    <div class="coverage">
      <p class="coverage__line">Your Car Covered with</p>
      <p class="coverage__amount">$100k</p>
      <p class="coverage__line">of Commercial Insurance</p>
    </div>

    <div class="partner partner--vortan">Vortan</div>
    <div class="partner partner--brenn"><span class="partner__dot"></span>Brenn</div>
    <div class="partner partner--dorvane">Dorvane</div>
    <div class="partner partner--twelve">12-Forty</div>
    <div class="partner partner--tesmira">Tesmira</div>
    <div class="partner partner--boltnest">BoltNest</div>

    <footer class="footer-band">
      <p class="footer-band__member">Member Dunmore Chamber of Commerce / Honest Merchant League</p>
      <p class="footer-band__web">www.willowcrestmotormate.example</p>
    </footer>
  </main>
</body>
</html>
```